Brand new website for global research and investment startup

We need a simple website, maybe 3 pages: landing page with business description, investment philosophy, team and contact info.
We have a logo already that can be incorporated. Please use the logo only, not the text
We like the color green, something along the lines of #3D6C32 as the main color.
We'd like to design the website with geometric shapes in gradations of the base color. The shapes should suggest "work in progress", "built to last (a long time)", "solidity" and "indestructibility". One idea floating in my head sees smaller features with icosahedron and dodecahedron shapes, and maybe larger structures like crystal lattices; but please feel free to be creative and imagine your own.

```html
<!DOCTYPE html>
<html lang="en">
<head>
<meta charset="utf-8">
<title>Halden Reach — Building Value That Endures</title>
<link rel="stylesheet" href="https://fonts.googleapis.com/css2?family=Plus+Jakarta+Sans:wght@400;500;600;700&family=Inter:wght@400;500;600&display=swap">
<style>
:root{
  --green:#3d6c32;
  --green-bright:#4d8a3e;
  --green-light:#5f9c4c;
  --ink:#1c1f1c;
  --dark:#141a15;
  --dark-2:#1f2620;
  --paper:#f4f6f1;
  --white:#ffffff;
  --muted:#5f655f;
  --line:#d9ddd6;
}
*{box-sizing:border-box;margin:0;padding:0}
html,body{width:1200px;height:3272px;overflow:hidden}
body{position:relative;font-family:"Inter",sans-serif;color:var(--ink);background:var(--white)}
.abs{position:absolute}
h1,h2,h3,.display{font-family:"Plus Jakarta Sans",sans-serif}

/* nav */
.site-nav{position:absolute;left:0;top:0;width:1200px;height:64px;border-bottom:1px solid rgba(255,255,255,.08);z-index:3}
.brand{position:absolute;display:flex;align-items:center;gap:10px;color:var(--white);font-family:"Plus Jakarta Sans",sans-serif;font-weight:600}
.brand .dot{border-radius:50%;background:var(--green-bright)}
.site-nav .brand{left:108px;top:18px;font-size:17px}
.site-nav .brand .dot{width:26px;height:26px}
.nav-links a{position:absolute;top:24px;font-size:12px;color:var(--white);text-decoration:none}
.nav-links a.active{color:var(--green-light)}
.btn{position:absolute;display:flex;align-items:center;justify-content:center;background:var(--green);color:var(--white);font-size:12px;font-weight:600;border-radius:4px;text-decoration:none}

/* hero */
.hero{position:absolute;left:0;top:0;width:1200px;height:640px;background:
  radial-gradient(ellipse 420px 300px at 880px 230px,rgba(61,108,50,.55),transparent 70%),
  radial-gradient(ellipse 500px 260px at 340px 330px,rgba(61,108,50,.35),transparent 70%),
  var(--dark)}
.hero-art{position:absolute;inset:0}
.hero h1{position:absolute;left:0;width:1200px;top:140px;text-align:center;font-size:50px;line-height:57px;font-weight:700;color:var(--white);letter-spacing:-.5px}
.hero h1 .accent{color:var(--green-bright)}
.hero p{position:absolute;left:0;width:1200px;top:338px;text-align:center;font-size:15px;line-height:22px;color:#e8ece6}
.hero-shape{position:absolute;left:0;top:540px}

/* about */
.about{position:absolute;left:0;top:620px;width:1200px;height:540px;background:var(--paper)}
.photo{position:absolute;border-radius:8px}
.eyebrow{position:absolute;font-size:15px;font-weight:600;color:var(--green);letter-spacing:.3px}
.about h2{position:absolute;left:600px;top:140px;font-size:38px;font-weight:700}
.about p{position:absolute;left:600px;top:208px;width:470px;font-size:12px;line-height:20px;color:var(--muted)}

/* philosophy */
.philosophy{position:absolute;left:0;top:1160px;width:1200px;height:552px;background:
  radial-gradient(ellipse 500px 250px at 600px 80px,#eef0ec,transparent),#f5f6f4}
.philosophy h2{position:absolute;left:0;width:1200px;top:92px;text-align:center;font-size:48px;font-weight:700;letter-spacing:-.5px}
.philosophy h2 span{color:var(--green)}
.value-card{position:absolute;top:197px;width:232px;height:270px;background:var(--white);border-radius:6px;box-shadow:0 2px 8px rgba(0,0,0,.08);overflow:hidden}
.value-card .photo{position:static;display:block;height:154px;border-radius:0}
.value-card h3{margin:26px 13px 0;font-size:14px;font-weight:700}
.value-card p{margin:12px 13px 0;font-size:11.5px;line-height:17px;color:var(--muted)}

/* team */
.team{position:absolute;left:0;top:1712px;width:1200px;height:574px;background:var(--green)}
.team h2{position:absolute;left:0;width:1200px;top:74px;text-align:center;font-size:48px;font-weight:700;color:var(--white)}
.member{position:absolute;top:177px;width:317px}
.member .photo{position:static;display:block;height:241px;border-radius:4px}
.member h3{margin-top:14px;font-size:24px;font-weight:700;color:var(--white)}
.member p{margin-top:12px;font-size:12px;color:#e5ede3}

/* contact */
.contact{position:absolute;left:0;top:2286px;width:1200px;height:600px;background:var(--white)}
.contact h2{position:absolute;left:0;width:1200px;top:110px;text-align:center;font-size:38px;font-weight:700}
.info-row{position:absolute;left:286px;display:flex;align-items:center;gap:14px}
.info-row .icon{width:28px;height:28px;border-radius:50%;background:#eef3ec;display:flex;align-items:center;justify-content:center}
.info-row b{display:block;font-weight:500;font-size:13px;line-height:14px}
.info-row span{font-size:11px}
.field{position:absolute;left:576px;width:340px;border:1px solid var(--line);border-radius:4px;font-size:11px;color:var(--muted);padding:12px 9px}
.field svg{position:absolute;right:14px;top:11px}

/* footer */
.site-footer{position:absolute;left:0;top:2860px;width:1200px;height:412px}
.footer-bg{position:absolute;left:0;top:0}
.site-footer .brand{left:108px;top:128px;font-size:32px;font-weight:500;letter-spacing:.5px}
.site-footer .brand .dot{width:44px;height:44px}
.footer-about{position:absolute;left:108px;top:190px;width:230px;font-size:11.5px;line-height:20px;color:#5e675f}
.footer-col h4{position:absolute;top:124px;font-family:"Plus Jakarta Sans",sans-serif;font-size:18px;font-weight:500;color:var(--white)}
.footer-col h4::after{content:"";position:absolute;left:0;bottom:-7px;width:28px;height:2px;background:var(--green-bright)}
.footer-link{position:absolute;font-size:11.5px;color:var(--white)}
.social{position:absolute;left:950px;width:40px;height:40px;border-radius:50%;background:var(--green)}
.copyright{position:absolute;left:0;width:1200px;top:386px;text-align:center;font-size:11.5px;color:#dfe4dd}
</style>
</head>
<body>

<header class="hero">
  <svg class="hero-art" width="1200" height="640" aria-hidden="true">
    <polygon points="700,120 1010,60 1100,260 880,420 640,330" fill="rgba(77,138,62,.18)"/>
    <polygon points="880,120 1040,180 960,330" fill="rgba(77,138,62,.22)"/>
    <polygon points="160,300 330,240 420,420 240,470" fill="rgba(61,108,50,.14)"/>
  </svg>
  <h1><span class="accent">BUILDING</span><br>VALUE THAT<br>ENDURES</h1>
  <p>Long-term investment strategies built on<br>patience, discipline, and conviction.</p>
  <a class="btn" style="left:543px;top:410px;width:114px;height:33px">Learn More</a>
  <svg class="hero-shape" width="1200" height="100" aria-hidden="true">
    <polygon points="0,72 275,20 875,85 1200,3 1200,100 0,100" fill="var(--paper)"/>
    <polyline points="0,70 240,26" stroke="var(--green)" stroke-width="3" fill="none"/>
    <polyline points="955,65 1200,1" stroke="var(--green)" stroke-width="3" fill="none"/>
  </svg>
</header>

<nav class="site-nav">
  <div class="brand"><span class="dot"></span>HALDEN REACH</div>
  <div class="nav-links">
    <a class="active" style="left:643px">Home</a>
    <a style="left:717px">Philosophy</a>
    <a style="left:820px">Team</a>
    <a style="left:892px">Contact</a>
  </div>
  <a class="btn" style="left:978px;top:14px;width:114px;height:34px">Get In Touch</a>
</nav>

<section class="about">
  <div class="photo" role="img" aria-label="Tablet showing a trading chart" style="left:115px;top:89px;width:275px;height:304px;background:linear-gradient(135deg,#2a3140,#1b3c6a 45%,#c8a23a 55%,#0f1c30)"></div>
  <div class="photo" role="img" aria-label="Glass office towers seen from below" style="left:305px;top:158px;width:247px;height:272px;background:linear-gradient(160deg,#c9d9ea,#7f93a8 40%,#2c3138 75%,#5a4230)"></div>
  <div class="eyebrow" style="left:600px;top:118px">ABOUT</div>
  <h2>Who we Are</h2>
  <p>Lorem ipsum dolor sit amet, consectetur adipiscing elit. Nunc finibus sit amet velit ac consectetur. Ut nec hendrerit lectus. Proin et facilisis sem. Vestibulum ante ipsum primis in faucibus orci luctus et ultrices posuere cubilia curae; Vestibulum ut dui non mauris commodo pulvinar. Aliquam laoreet gravida lorem nec luctus. Proin tincidunt urna ut molestie molestie. Mauris sit amet volutpat ex, in laoreet odio. Nullam ac nisl nec justo convallis faucibus. Phasellus luctus consectetur ex, sed pharetra ligula varius at. Interdum et malesuada fames ac ante ipsum primis in faucibus. Donec tempor justo et facilisis scelerisque.</p>
  <a class="btn" style="left:600px;top:390px;width:114px;height:33px">Learn More</a>
</section>

<section class="philosophy">
  <h2>Our Investment <span>Philosophy</span></h2>
  <article class="value-card" style="left:109px">
    <div class="photo" role="img" aria-label="Hourglass standing on pebbles" style="background:linear-gradient(180deg,#4a3a33,#8a6f5d 60%,#6b5040)"></div>
    <h3>Patience</h3>
    <p>We measure outcomes in decades, not quarters. Time is the compounding engine.</p>
  </article>
  <article class="value-card" style="left:359px">
    <div class="photo" role="img" aria-label="Martial artist in a white uniform, head bowed" style="background:linear-gradient(90deg,#d9d9d9,#a9a9a9 55%,#3a3a3a)"></div>
    <h3>Discipline</h3>
    <p>A written process, consistently applied, regardless of the mood of the market.</p>
  </article>
  <article class="value-card" style="left:609px">
    <div class="photo" role="img" aria-label="Person in a blue sweater with a fist on the chest" style="background:linear-gradient(90deg,#cfd3d8,#5c74b4 45%,#4a62a3 70%,#c8ccd0)"></div>
    <h3>Conviction</h3>
    <p>Few positions, deeply understood. We invest only where our research is decisive.</p>
  </article>
  <article class="value-card" style="left:859px">
    <div class="photo" role="img" aria-label="Team joining hands over a table of reports" style="background:linear-gradient(135deg,#2a2e3a,#7b7a80 50%,#d9d6d2)"></div>
    <h3>Integrity</h3>
    <p>Our capital sits alongside yours. Alignment is structural, not stated.</p>
  </article>
</section>

<section class="team">
  <h2>Our Team</h2>
  <div class="member" style="left:108px">
    <div class="photo" role="img" aria-label="Portrait of the managing partner" style="background:linear-gradient(180deg,#e8e8e8,#dcdcdc 55%,#7a2a44)"></div>
    <h3>Marta Quell</h3><p>Managing Partner</p>
  </div>
  <div class="member" style="left:442px">
    <div class="photo" role="img" aria-label="Portrait of the chief investment officer" style="background:linear-gradient(180deg,#3a2e2a,#2a2424 55%,#151a24)"></div>
    <h3>Oskar Lindqvist</h3><p>Chief Investment Officer</p>
  </div>
  <div class="member" style="left:775px">
    <div class="photo" role="img" aria-label="Portrait of the head of research" style="background:linear-gradient(180deg,#b4b4b4,#8a8a8a 55%,#3a3a3c)"></div>
    <h3>Jonah Pereira</h3><p>Head of Research</p>
  </div>
</section>

<section class="contact">
  <div class="eyebrow" style="left:0;width:1200px;text-align:center;top:84px">GET IN TOUCH</div>
  <h2>Begin a conversation</h2>

  <div class="info-row" style="top:282px">
    <div class="icon"><svg width="14" height="14" viewBox="0 0 24 24" fill="none" stroke="#3d6c32" stroke-width="2"><path d="M12 22s7-7 7-12a7 7 0 0 0-14 0c0 5 7 12 7 12z"/><circle cx="12" cy="10" r="2.5"/></svg></div>
    <div><b>Address</b><span>42 Larchmont Row, Easthaven EH4 2QP</span></div>
  </div>
  <div class="info-row" style="top:342px">
    <div class="icon"><svg width="14" height="14" viewBox="0 0 24 24" fill="none" stroke="#3d6c32" stroke-width="2"><path d="M5 3h4l2 5-2.5 1.5a11 11 0 0 0 6 6L16 13l5 2v4a2 2 0 0 1-2 2A17 17 0 0 1 3 5a2 2 0 0 1 2-2z"/></svg></div>
    <div><b>Phone</b><span>+00 11 2233 4455</span></div>
  </div>
  <div class="info-row" style="top:402px">
    <div class="icon"><svg width="14" height="14" viewBox="0 0 24 24" fill="none" stroke="#3d6c32" stroke-width="2"><rect x="3" y="5" width="18" height="14" rx="2"/><path d="M3 7l9 6 9-6"/></svg></div>
    <div><b>Email</b><span>hello@haldenreach.example</span></div>
  </div>

  <div class="field" style="top:204px;height:38px">Name<svg width="16" height="16" viewBox="0 0 24 24" fill="none" stroke="#777" stroke-width="1.5"><circle cx="12" cy="8" r="4"/><path d="M4 21c1-4 4-6 8-6s7 2 8 6z"/></svg></div>
  <div class="field" style="top:264px;height:38px">Email<svg width="18" height="16" viewBox="0 0 24 24" fill="none" stroke="#777" stroke-width="1.5"><rect x="3" y="5" width="18" height="14" rx="2"/><path d="M3 7l9 6 9-6"/></svg></div>
  <div class="field" style="top:324px;height:36px">Phone Number<svg width="16" height="16" viewBox="0 0 24 24" fill="none" stroke="#777" stroke-width="1.5"><path d="M5 3h4l2 5-2.5 1.5a11 11 0 0 0 6 6L16 13l5 2v4a2 2 0 0 1-2 2A17 17 0 0 1 3 5a2 2 0 0 1 2-2z"/></svg></div>
  <div class="field" style="top:380px;height:68px">Name<svg width="16" height="16" viewBox="0 0 24 24" fill="none" stroke="#777" stroke-width="1.5"><path d="M21 12a8 8 0 0 1-12 7l-5 1 1-4a8 8 0 1 1 16-4z"/></svg></div>
  <a class="btn" style="left:576px;top:474px;width:114px;height:34px">Send Now</a>
</section>

<footer class="site-footer">
  <svg class="footer-bg" width="1200" height="412" aria-hidden="true">
    <defs>
      <radialGradient id="footerGlow" cx="50%" cy="100%" r="70%">
        <stop offset="0" stop-color="#1e3a2c"/><stop offset="1" stop-color="#1a1f1b"/>
      </radialGradient>
    </defs>
    <polygon points="0,62 324,14 870,60 1200,56 1200,412 0,412" fill="#2a302b"/>
    <polygon points="0,62 1200,60 1200,412 0,412" fill="url(#footerGlow)"/>
  </svg>
  <div class="brand"><span class="dot"></span>HALDEN REACH</div>
  <p class="footer-about">Lorem ipsum dolor sit amet, consectetur adipiscing elit. Nunc finibus sit amet velit ac consectetur. Ut nec hendrerit lectus. Proin et facilisis sem.</p>

  <div class="footer-col"><h4 style="left:444px">Quick Links</h4></div>
  <span class="footer-link" style="left:444px;top:170px">Home</span>
  <span class="footer-link" style="left:444px;top:201px">About</span>
  <span class="footer-link" style="left:444px;top:232px">Philosophy</span>
  <span class="footer-link" style="left:444px;top:263px">Team</span>
  <span class="footer-link" style="left:444px;top:294px">Contact</span>

  <div class="footer-col"><h4 style="left:652px">Contact Detail</h4></div>
  <span class="footer-link" style="left:652px;top:172px"><svg width="12" height="14" viewBox="0 0 24 24" fill="#4d8a3e"><path d="M12 22s7-7 7-12a7 7 0 0 0-14 0c0 5 7 12 7 12z"/></svg> 42 Larchmont Row, Easthaven EH4 2QP</span>
  <span class="footer-link" style="left:652px;top:215px"><svg width="14" height="14" viewBox="0 0 24 24" fill="#4d8a3e"><path d="M5 3h4l2 5-2.5 1.5a11 11 0 0 0 6 6L16 13l5 2v4a2 2 0 0 1-2 2A17 17 0 0 1 3 5a2 2 0 0 1 2-2z"/></svg> +00 11 2233 4455</span>
  <span class="footer-link" style="left:652px;top:250px"><svg width="14" height="12" viewBox="0 0 24 20" fill="#4d8a3e"><rect x="1" y="1" width="22" height="18" rx="2"/></svg> hello@haldenreach.example</span>

  <div class="footer-col"><h4 style="left:950px">Follow Us</h4></div>
  <span class="social" style="top:165px" role="img" aria-label="Social profile"></span>
  <span class="social" style="top:216px" role="img" aria-label="Social profile"></span>
  <span class="social" style="top:268px" role="img" aria-label="Social profile"></span>

  <p class="copyright">© 2026 Demo. All rights reserved.</p>
</footer>

</body>
</html>
```